Oven Cleaning flyer design

Hi there,
I need help designing a letterbox flyer. It needs to be DL size.
I have attached a rough design made with Chat GPT.
Would like back and front, have my business colors.
Please find attached mock up of what I would roughly like.
Also find attached logo.
Thank you

Target Market(s)

Home owners over 40

Industry/Entity Type

Cleaning

Requirements
Must have
• Logo, before after of oven, brand colors

```html
<!DOCTYPE html>
<html lang="en">
<head>
<meta charset="utf-8">
<title>Gleam Oven Care – DL Flyer</title>
<link rel="stylesheet" href="https://fonts.googleapis.com/css2?family=Montserrat:wght@400;500;600;700;800&display=swap">
<style>
  :root{
    --teal:#3cc3cf;
    --sky:#1e9be0;
    --navy:#1c2a5c;
    --navy-light:#1f6fae;
    --ink:#111111;
    --white:#ffffff;
    --stage:#7a7a7a;
    --stage-dark:#2e2e2e;
  }
  *{margin:0;padding:0;box-sizing:border-box}
  html,body{width:1200px;height:2291px;overflow:hidden}
  body{
    background:linear-gradient(135deg,var(--stage-dark) 0%,var(--stage) 50%,var(--stage-dark) 100%);
    font-family:"Montserrat",sans-serif;
    position:relative;
  }
  .flyer{
    position:absolute;top:593px;width:520px;height:1104px;
    background:var(--white);overflow:hidden;
    box-shadow:0 12px 30px rgba(0,0,0,.45);
  }
  .flyer--front{left:53px}
  .flyer--back{left:627px}
  .flyer__art{position:absolute;inset:0;width:520px;height:1104px}
  .brand{
    position:absolute;top:46px;left:0;width:100%;
    display:flex;align-items:center;justify-content:center;gap:16px;
  }
  .brand__dot{width:70px;height:70px;border-radius:50%;background:var(--teal)}
  .brand__name{color:var(--teal);font-weight:800;font-size:34px;letter-spacing:1px;white-space:nowrap}
  .hero{position:absolute;top:150px;left:0;width:100%;text-align:center}
  .hero__lead{color:var(--teal);font-size:56px;font-weight:500;line-height:1;letter-spacing:-1px}
  .hero__title{color:var(--ink);font-size:56px;font-weight:800;line-height:1.02;letter-spacing:-1px}
  .hero__text{margin:12px auto 0;width:380px;font-size:17px;line-height:1.35;color:var(--ink)}
  .photo-label{position:absolute;top:755px;color:var(--white);font-weight:800;font-size:26px;letter-spacing:.5px}
  .photo-label--before{left:82px}
  .photo-label--after{left:312px}
  .cta{position:absolute;left:0;width:100%;text-align:center;color:var(--white)}
  .flyer--front .cta,.flyer--back .cta{top:900px}
  .cta__line{font-size:28px;font-weight:600;line-height:1.2}
  .cta__phone{
    margin-top:12px;display:flex;align-items:center;justify-content:center;gap:10px;
    color:var(--teal);font-weight:800;font-size:50px;line-height:1;letter-spacing:.5px;
  }
  .cta__phone svg{width:46px;height:46px}
  .cta__web{
    margin-top:18px;display:flex;align-items:center;justify-content:center;gap:8px;
    color:var(--teal);font-weight:700;font-size:22px;
  }
  .cta__web svg{width:24px;height:24px}
  .why{position:absolute;top:178px;left:48px;width:432px}
  .why__title{font-size:32px;line-height:1.05;color:var(--ink);font-weight:500}
  .why__title strong{font-weight:700}
  .why__text{margin-top:16px;font-size:16px;line-height:1.55;text-align:justify;color:var(--ink)}
  .offer{position:absolute;top:432px;left:42px}
  .offer__amount{color:var(--teal);font-size:82px;font-weight:800;line-height:1;letter-spacing:-2px}
  .offer__amount span{font-weight:600}
  .offer__sub{font-size:32px;font-weight:600;color:var(--ink);margin-left:6px;line-height:1}
  .perks{position:absolute;top:588px;left:48px;list-style:none}
  .perks li{display:flex;align-items:center;gap:12px;font-weight:700;font-size:18px;height:34px;color:var(--ink)}
  .perks svg{width:24px;height:24px}
  .also{position:absolute;top:712px;left:0;width:100%;text-align:center;color:var(--teal);font-size:29px;font-weight:500;line-height:1.12}
  .also strong{font-weight:700}
</style>
</head>
<body>

<svg width="0" height="0" style="position:absolute" aria-hidden="true">
  <defs>
    <symbol id="sparkle" viewBox="-10 -10 20 20">
      <path d="M0 -10 Q0.8 -0.8 10 0 Q0.8 0.8 0 10 Q-0.8 0.8 -10 0 Q-0.8 -0.8 0 -10Z"/>
    </symbol>
    <linearGradient id="navyBand" x1="0" y1="0" x2="1" y2="0.4">
      <stop offset="0" stop-color="#1f7cb8"/>
      <stop offset="0.55" stop-color="#1c3d78"/>
      <stop offset="1" stop-color="#1c2a5c"/>
    </linearGradient>
    <linearGradient id="beforeTone" x1="0" y1="0" x2="0.4" y2="1">
      <stop offset="0" stop-color="#5d5f63"/>
      <stop offset="0.6" stop-color="#6b4a2c"/>
      <stop offset="1" stop-color="#8a8c90"/>
    </linearGradient>
    <linearGradient id="afterTone" x1="0" y1="0" x2="0" y2="1">
      <stop offset="0" stop-color="#d9dcdf"/>
      <stop offset="0.5" stop-color="#9ea3a8"/>
      <stop offset="1" stop-color="#e6e8ea"/>
    </linearGradient>
    <symbol id="phoneIcon" viewBox="0 0 48 48">
      <circle cx="24" cy="24" r="22" fill="#fff"/>
      <path d="M17 12c1-1 3-1 4 1l3 5c.5 1 .2 2.2-.6 3l-2 1.6c1.5 3.2 3.8 5.6 7 7l1.6-2c.8-.8 2-1.1 3-.6l5 3c2 1 2 3 1 4l-2 2c-2 2-6 2-10-1-5-3-9-8-11-13-1.5-4-1-7 1-9z" fill="#1c2a5c"/>
    </symbol>
    <symbol id="globeIcon" viewBox="0 0 24 24">
      <g fill="none" stroke="#fff" stroke-width="1.6">
        <circle cx="12" cy="12" r="10"/>
        <ellipse cx="12" cy="12" rx="4.5" ry="10"/>
        <path d="M2 12h20M4 6.5h16M4 17.5h16"/>
      </g>
    </symbol>
  </defs>
</svg>

<!-- Front -->
<section class="flyer flyer--front">
  <svg class="flyer__art" viewBox="0 0 520 1104" aria-hidden="false">
    <rect x="0" y="380" width="262" height="480" fill="url(#beforeTone)" role="img" aria-label="Photo of a dirty oven interior with burnt grease (before)"/>
    <rect x="262" y="380" width="258" height="480" fill="url(#afterTone)" role="img" aria-label="Photo of the same oven cleaned and gleaming (after)"/>
    <rect x="259" y="380" width="5" height="480" fill="#fff"/>
    <path d="M0 0H520V360C520 475 380 510 230 510C120 510 30 480 0 440Z" fill="#111"/>
    <path d="M0 0H520V320C515 430 380 475 230 475C120 475 30 445 0 400Z" fill="#fff"/>
    <path d="M0 465C60 515 150 535 240 535C380 535 490 495 520 395" fill="none" stroke="#3cc3cf" stroke-width="4"/>
    <path d="M430 70C480 100 515 150 520 210" fill="none" stroke="#111" stroke-width="6"/>
    <path d="M0 1104V905C60 825 180 790 300 790C400 790 480 815 520 845V1104Z" fill="#111"/>
    <path d="M0 1104V935C60 855 180 820 300 820C400 820 480 845 520 875V1104Z" fill="url(#navyBand)"/>
    <path d="M0 950C70 860 190 832 300 832C410 832 480 858 520 888" fill="none" stroke="#3cc3cf" stroke-width="4"/>
    <g fill="#1e9be0">
      <use href="#sparkle" x="65" y="490" width="70" height="70"/>
      <use href="#sparkle" x="135" y="460" width="46" height="46"/>
      <use href="#sparkle" x="113" y="565" width="22" height="22"/>
      <use href="#sparkle" x="368" y="790" width="70" height="70"/>
      <use href="#sparkle" x="430" y="770" width="46" height="46"/>
      <use href="#sparkle" x="418" y="870" width="26" height="26"/>
    </g>
  </svg>

  <div class="brand"><span class="brand__dot"></span><span class="brand__name">GLEAM OVEN CARE</span></div>

  <div class="hero">
    <div class="hero__lead">Bring Your Oven</div>
    <div class="hero__title">Back to Life</div>
    <p class="hero__text">Professional, non-caustic oven cleaning that removes built-up grease, smoke, and burnt grime-leaving your oven looking fresh again.</p>
  </div>

  <span class="photo-label photo-label--before">BEFORE</span>
  <span class="photo-label photo-label--after">AFTER</span>

  <div class="cta">
    <div class="cta__line">Call Now for</div>
    <div class="cta__line">Fast, Professional Service</div>
    <div class="cta__phone"><svg><use href="#phoneIcon"/></svg>0400 000 123</div>
    <div class="cta__web"><svg><use href="#globeIcon"/></svg>www.gleamovencare.com.au</div>
  </div>
</section>

<!-- Back -->
<section class="flyer flyer--back">
  <svg class="flyer__art" viewBox="0 0 520 1104" aria-hidden="true">
    <path d="M0 1104V905C60 825 180 790 300 790C400 790 480 815 520 845V1104Z" fill="#111"/>
    <path d="M0 1104V935C60 855 180 820 300 820C400 820 480 845 520 875V1104Z" fill="url(#navyBand)"/>
    <path d="M0 950C70 860 190 832 300 832C410 832 480 858 520 888" fill="none" stroke="#3cc3cf" stroke-width="4"/>
    <g fill="#1e9be0">
      <use href="#sparkle" x="368" y="775" width="70" height="70"/>
      <use href="#sparkle" x="440" y="760" width="46" height="46"/>
      <use href="#sparkle" x="418" y="868" width="26" height="26"/>
    </g>
  </svg>

  <div class="brand"><span class="brand__dot"></span><span class="brand__name">GLEAM OVEN CARE</span></div>

  <div class="why">
    <h2 class="why__title"><strong>why choose</strong><br>Gleam Oven Care?</h2>
    <p class="why__text">we're a local family business providing professional, non-caustic oven cleaning across Sunshine Coast. Using specialized-equipment and proven cleaning methods, we remove heavy grease, carbon build-up. smoke residue, restoring your oven safely and effectively.</p>
  </div>

  <div class="offer">
    <div class="offer__amount">$10 <span>off</span></div>
    <div class="offer__sub">your first clean</div>
  </div>

  <ul class="perks">
    <li><svg viewBox="0 0 20 20" fill="#1e9be0"><use href="#sparkle"/></svg>Reliable Service</li>
    <li><svg viewBox="0 0 20 20" fill="#1e9be0"><use href="#sparkle"/></svg>Non-Caustic Cleaning</li>
    <li><svg viewBox="0 0 20 20" fill="#1e9be0"><use href="#sparkle"/></svg>Satisfaction Guaranteed</li>
  </ul>

  <p class="also">We also clean <strong>cooktops,</strong><br><strong>rangehoods</strong> and <strong>BBQs</strong></p>

  <div class="cta">
    <div class="cta__line">Call Now for</div>
    <div class="cta__line">Fast, Professional Service</div>
    <div class="cta__phone"><svg><use href="#phoneIcon"/></svg>0400 000 123</div>
    <div class="cta__web"><svg><use href="#globeIcon"/></svg>www.gleamovencare.com.au</div>
  </div>
</section>

</body>
</html>
```